LINGERIE WEBSHOP - Velora casa

We are looking for design and layout design for our webshop. We are company that sells lingerie and other connected textile products liki payamas and etc..
Our website will have approx 500 different products within 2 main catogories Woman/Man) and approx. 10 subcategories
Here is what we expect form design:
-Color pallete should be black and white (if you wish you can add some accent color)
-we want to leave feeling to customers of good quality products towards to luxury
-UX should be simple. Feel free to suggest layout
-frontpage layout, product list layout, product description layout, blog layout
-responsive design, compatible with smartphone

Target Market(s)

woman buying for themself, man buying for woman

Industry/Entity Type

Lingerie

Logo Text

VELORA CASA

Number of Pages Required

4 page

Font styles to use
Sans Serif
Decorative

Requirements
Must have
• simple UX
Nice to have
• difference for sexy/luxury lingerie and daily/cozy lingerie
Should not have
• cheap feel, unreliable

```html
<!DOCTYPE html>
<html lang="en">
<head>
<meta charset="utf-8">
<title>Velora Casa — Lingerie Webshop</title>
<link href="https://fonts.googleapis.com/css2?family=Roboto:wght@300;400;500;700;900&family=Roboto+Slab:wght@400&display=swap" rel="stylesheet">
<style>
:root{
  --accent:#f47c20;
  --ink:#222222;
  --text:#555555;
  --muted:#8a8a8a;
  --line:#e3e3e3;
  --soft:#f1f1f1;
  --blog-bg:#f6f6f6;
  --pink:#f48a93;
  --footer:#1d1d1d;
  --white:#ffffff;
}
*{box-sizing:border-box;margin:0;padding:0}
html,body{width:1200px;height:5159px;overflow:hidden}
body{position:relative;font-family:'Roboto',sans-serif;color:var(--text);background:var(--white)}
.abs{position:absolute}
.btn{position:absolute;display:flex;align-items:center;justify-content:center;background:var(--accent);color:var(--white);font-weight:700;font-size:12px;letter-spacing:.5px;border-radius:18px}
.photo{position:absolute}

/* top bar */
.topbar{position:absolute;left:0;top:0;width:1200px;height:30px;background:var(--accent);color:var(--white);font-size:13px}
.topbar span{position:absolute;top:7px;display:flex;align-items:center;gap:7px}
/* header */
.header{position:absolute;left:0;top:30px;width:1200px;height:96px;background:var(--white)}
.logo{position:absolute;left:142px;top:34px;font-weight:300;font-size:28px;letter-spacing:1px;color:var(--ink)}
.nav{position:absolute;left:428px;top:45px;display:flex;gap:33px;font-size:13px;font-weight:500;color:var(--ink)}
.nav .active{color:var(--accent)}
/* hero */
.hero{position:absolute;left:0;top:126px;width:1200px;height:631px;background:linear-gradient(100deg,#d8d6d4 0%,#b48a6a 30%,#ebe8e5 55%,#f0efed 100%)}
.hero-title{position:absolute;left:0;width:1200px;top:54px;text-align:center;font-size:50px;font-weight:900;color:var(--ink)}
.hero-text{position:absolute;left:420px;width:360px;top:120px;text-align:center;font-size:15px;line-height:24px;color:#444}
.arrow{position:absolute;width:40px;height:40px;border-radius:50%;border:2px solid rgba(255,255,255,.9)}
.arrow.dark{border:1px solid #555;width:34px;height:34px}
/* features */
.features{position:absolute;left:0;top:757px;width:1200px;height:116px;background:#efefef}
.feat{position:absolute;top:36px}
.feat h4{font-size:14px;font-weight:700;color:var(--ink);margin-bottom:5px}
.feat p{font-size:13px;color:var(--text)}
.feat svg{position:absolute;left:-60px;top:-2px}
/* categories */
.cat{position:absolute;top:873px;width:398px;height:281px;background:var(--soft)}
.cat .photo{left:0;top:0;width:226px;height:281px}
.cat h3{position:absolute;left:228px;top:56px;font-size:17px;font-weight:700;color:var(--ink)}
.cat p{position:absolute;left:228px;top:86px;width:156px;font-size:12.5px;line-height:22px;color:var(--text)}
.cat .btn{left:228px;top:187px;width:124px;height:32px;font-size:11px}
/* section titles */
.sec-title{position:absolute;left:0;width:1200px;text-align:center;font-size:36px;font-weight:700;color:var(--ink)}
.sec-rule{position:absolute;left:565px;width:70px;height:3px;background:var(--accent)}
/* product cards */
.card{position:absolute;width:208px;background:var(--white);box-shadow:0 2px 10px rgba(0,0,0,.14);padding:7px}
.card .photo{position:relative;width:194px;height:252px}
.heart{position:absolute;right:14px;top:14px;width:24px;height:24px;border-radius:50%;background:var(--accent)}
.heart svg{position:absolute;left:6px;top:7px}
.card .name{margin-top:18px;text-align:center;font-family:'Roboto Slab',serif;font-size:15px;line-height:20px;color:#333}
.card .price{margin-top:12px;text-align:center;font-size:13px}
.card .price s{color:#666;margin-right:8px}
.card .price b{color:var(--accent);font-weight:400}
.card .btn{position:relative;margin:14px auto 14px;width:124px;height:30px;font-size:11px}
/* sale */
.sale{position:absolute;left:0;top:1903px;width:1200px;height:535px;background:linear-gradient(180deg,#b6cfe2 0%,#dfe6ea 25%,#e6ddd3 45%,#d8c9b6 100%)}
.sale-word{position:absolute;font-size:112px;font-weight:900;color:#3b3b3b;letter-spacing:2px;line-height:1}
.badge{position:absolute;left:771px;top:2087px;width:192px;height:192px;border-radius:50%;background:var(--accent);border:4px solid rgba(255,255,255,.7);color:var(--white);text-align:center}
/* about */
.about{position:absolute;left:0;top:2438px;width:1200px;height:529px;background:linear-gradient(90deg,#8c9a6c 0%,#a8b38e 40%,#c9cdb8 65%,#6c6d62 100%)}
.about-frame{position:absolute;left:142px;top:2540px;width:450px;height:340px;border:2px solid #e6c8a8}
.about-box{position:absolute;left:150px;top:2540px;width:442px;height:332px;background:var(--white);padding:34px 30px}
.about-box h2{font-size:34px;font-weight:500;line-height:38px;color:var(--ink)}
.about-box p{margin-top:18px;font-size:13.5px;line-height:22.5px;color:var(--text)}
.about-box .btn{position:relative;margin-top:18px;width:150px;height:40px;border-radius:2px;font-size:13px}
/* blog */
.blog{position:absolute;left:0;top:3636px;width:1200px;height:701px;background:var(--blog-bg)}
.post{position:absolute;top:3800px;width:424px}
.post .photo{position:relative;width:424px;height:234px;border-radius:8px}
.date{position:absolute;left:0;top:262px;width:42px;height:42px;border-radius:50%;background:var(--accent);color:var(--white);text-align:center;font-size:18px;font-weight:500;line-height:18px;padding-top:7px}
.date small{display:block;font-size:7px;line-height:8px}
.post h3{position:absolute;left:66px;top:260px;width:360px;font-family:'Roboto Slab',serif;font-weight:400;font-size:19px;line-height:24px;color:#333}
.post .meta{position:absolute;left:66px;top:320px;font-size:12.5px;color:#555;display:flex;gap:26px}
.post .meta i{color:var(--accent);font-style:normal;margin-right:6px}
.post p{position:absolute;left:66px;top:346px;width:340px;font-size:12.5px;line-height:22px;color:#555}
.post .btn{left:66px;top:436px;width:122px;height:32px;background:#2b2b2b;font-size:10.5px;font-weight:500}
/* newsletter */
.news{position:absolute;left:0;top:4337px;width:1200px;height:332px;background:var(--pink)}
.news h2{position:absolute;left:142px;top:94px;font-size:28px;font-weight:700;color:var(--white);letter-spacing:.5px}
.news p{position:absolute;left:142px;top:138px;width:320px;font-size:14px;line-height:20px;color:var(--white)}
.news .field{position:absolute;left:142px;top:213px;width:440px;height:38px;border-radius:19px;background:var(--white);font-size:11.5px;color:#444;padding:12px 20px}
.news .btn{left:444px;top:213px;width:138px;height:38px;font-size:13px;border-radius:19px}
/* footer */
.footer{position:absolute;left:0;top:4669px;width:1200px;height:490px;background:var(--footer);color:#cfcfcf}
.footer h4{position:absolute;top:72px;font-size:17px;font-weight:700;color:var(--white)}
.footer ul{position:absolute;top:123px;list-style:none;font-size:13px;line-height:29px}
.contact{position:absolute;left:142px;font-size:13px;line-height:18px}
.contact svg{position:absolute;left:0;top:0}
.contact div{padding-left:38px}
.pay{position:absolute;top:4830px;width:48px;height:28px;border-radius:3px}
.soc{position:absolute;top:4872px;width:30px;height:30px;border-radius:50%;border:1.5px solid var(--white)}
.copy{position:absolute;left:0;width:1200px;top:5098px;text-align:center;font-size:13px;color:#d6d6d6}
</style>
</head>
<body>

<!-- top bar -->
<div class="topbar">
  <span style="left:142px"><svg width="11" height="9" viewBox="0 0 11 9"><path d="M1 4.5l3 3 6-6.5" stroke="#fff" stroke-width="2" fill="none"/></svg>30 Day Return Right</span>
  <span style="left:720px"><svg width="12" height="12" viewBox="0 0 12 12"><path d="M2.5 1l2 2.5-1 1.5c.7 1.5 1.8 2.6 3.3 3.3l1.5-1 2.5 2-1 2C5 11 1 7 .8 2z" fill="#fff"/></svg>01 / 5830-217</span>
  <span style="left:873px;font-weight:500"><svg width="11" height="12" viewBox="0 0 11 12"><rect x="1" y="5" width="9" height="7" fill="#fff"/><path d="M3 5V3.5a2.5 2.5 0 015 0V5" stroke="#fff" stroke-width="1.6" fill="none"/></svg>REGISTER</span>
  <span style="left:990px;font-weight:500"><svg width="12" height="12" viewBox="0 0 12 12"><circle cx="6" cy="6" r="6" fill="#fff"/><circle cx="6" cy="4.5" r="2" fill="#f47c20"/><path d="M2.5 10a4 3 0 017 0" fill="#f47c20"/></svg>LOGIN</span>
</div>

<!-- header -->
<header class="header">
  <div class="logo">VELORA CASA</div>
  <nav class="nav">
    <span class="active">HOME</span><span>ABOUT</span><span>WOMEN</span><span>MEN</span><span>CHILDREN</span><span>BLOG</span><span>CONTACT</span>
  </nav>
  <svg class="abs" style="left:988px;top:36px" width="30" height="28" viewBox="0 0 30 28"><path d="M1 3h5l4 15h14l3-10H8" stroke="#333" stroke-width="1.8" fill="none"/><circle cx="12" cy="23" r="2" fill="#333"/><circle cx="22" cy="23" r="2" fill="#333"/><circle cx="10" cy="4" r="5" fill="#f47c20"/></svg>
  <svg class="abs" style="left:1036px;top:42px" width="16" height="16" viewBox="0 0 16 16"><circle cx="6.5" cy="6.5" r="5" stroke="#333" stroke-width="2" fill="none"/><path d="M10 10l5 5" stroke="#333" stroke-width="2.4"/></svg>
</header>

<!-- hero -->
<section class="hero" role="img" aria-label="Photo of a man reclining in white underwear on a light studio background">
  <h1 class="hero-title">UNDERWEAR</h1>
  <p class="hero-text">Sed ut perspiciatis unde omnis iste natus sit voluptatem accusantium doloremque litium, totam rem aperiam</p>
  <div class="btn" style="left:528px;top:206px;width:146px;height:40px;border-radius:2px;font-size:13px">SHOP NOW</div>
  <div class="arrow" style="left:48px;top:276px"><svg width="36" height="36" viewBox="0 0 36 36"><path d="M21 11l-7 7 7 7" stroke="#fff" stroke-width="2" fill="none"/></svg></div>
  <div class="arrow" style="left:1110px;top:270px"><svg width="36" height="36" viewBox="0 0 36 36"><path d="M15 11l7 7-7 7" stroke="#fff" stroke-width="2" fill="none"/></svg></div>
</section>

<!-- features -->
<section class="features">
  <div class="feat" style="left:122px">
    <svg width="42" height="34" viewBox="0 0 42 34"><path d="M2 6h24v18H2zM26 12h8l6 7v5H26" stroke="#f47c20" stroke-width="2" fill="none"/><circle cx="10" cy="27" r="4" stroke="#f47c20" stroke-width="2" fill="#efefef"/><circle cx="32" cy="27" r="4" stroke="#f47c20" stroke-width="2" fill="#efefef"/></svg>
    <h4>FREE RETURNS</h4><p>Duis aute irure dolor in</p></div>
  <div class="feat" style="left:372px">
    <svg width="40" height="36" viewBox="0 0 40 36"><path d="M6 22v-6a14 14 0 0128 0v6" stroke="#f47c20" stroke-width="2.4" fill="none"/><rect x="4" y="18" width="8" height="12" rx="3" stroke="#f47c20" stroke-width="2" fill="none"/><rect x="28" y="18" width="8" height="12" rx="3" stroke="#f47c20" stroke-width="2" fill="none"/></svg>
    <h4>ONLINE SUPPORT</h4><p>Lorem ipsum dolor sit amet</p></div>
  <div class="feat" style="left:662px">
    <svg width="40" height="38" viewBox="0 0 40 38"><circle cx="20" cy="19" r="16" stroke="#f47c20" stroke-width="2.4" fill="none"/><path d="M20 10v9l6 5" stroke="#f47c20" stroke-width="2.4" fill="none"/></svg>
    <h4>48 HRS SHIPPING</h4><p>booking before kl. 16.30 Mon-Fri</p></div>
  <div class="feat" style="left:996px">
    <svg width="50" height="36" viewBox="0 0 50 36"><rect x="2" y="4" width="46" height="28" rx="2" stroke="#f47c20" stroke-width="2" fill="none"/><rect x="7" y="9" width="36" height="18" stroke="#f47c20" stroke-width="1.5" fill="none"/><circle cx="25" cy="18" r="6" stroke="#f47c20" stroke-width="2" fill="none"/></svg>
    <h4>EASY PAYMENT</h4><p>For purchases from 499</p></div>
</section>

<!-- categories -->
<section class="cat" style="left:0">
  <div class="photo" role="img" aria-label="Photo of a woman in pink patterned pyjamas" style="background:linear-gradient(160deg,#e9e2dc,#f1c3c8 60%,#e6a0aa)"></div>
  <h3>WOMEN</h3><p>By coming to Velora casa, you will enter the wonderful world of lingerie. Intimate</p>
  <div class="btn">LEARN MORE</div>
</section>
<section class="cat" style="left:401px">
  <div class="photo" role="img" aria-label="Photo of a man in a white vest and white briefs" style="background:linear-gradient(160deg,#eeeeee,#d8d4d0 60%,#c4a48a)"></div>
  <h3>MEN</h3><p>Men's underwear for the modern man made of the highest quality cotton, soft to</p>
  <div class="btn">LEARN MORE</div>
</section>
<section class="cat" style="left:802px">
  <div class="photo" role="img" aria-label="Photo of a toddler in pink pyjamas" style="background:linear-gradient(160deg,#eeeeee,#e6c8d2 55%,#d77aa0)"></div>
  <h3>CHILDREN</h3><p>We pay special attention to the children's range of underwear, aware that only top</p>
  <div class="btn">LEARN MORE</div>
</section>

<!-- featured products -->
<h2 class="sec-title" style="top:1228px">FEATURED PRODUCTS</h2>
<div class="sec-rule" style="top:1292px"></div>
<div class="arrow dark" style="left:75px;top:1521px"><svg width="32" height="32" viewBox="0 0 32 32"><path d="M18 10l-6 6 6 6" stroke="#444" stroke-width="1.6" fill="none"/></svg></div>
<div class="arrow dark" style="left:1090px;top:1521px"><svg width="32" height="32" viewBox="0 0 32 32"><path d="M14 10l6 6-6 6" stroke="#444" stroke-width="1.6" fill="none"/></svg></div>

<div class="card" style="left:142px;top:1346px">
  <div class="photo" role="img" aria-label="Product photo of a woman in a white lingerie set" style="background:linear-gradient(180deg,#e8e6e4,#c9a48c 60%,#e4e0dc)"><div class="heart"><svg width="12" height="11" viewBox="0 0 12 11"><path d="M6 10L1.2 5.2A2.8 2.8 0 016 1.4a2.8 2.8 0 014.8 3.8z" fill="#fff"/></svg></div></div>
  <div class="name">Nemo enim ipsam voluptatem quia volu</div>
  <div class="price"><s>$95.00</s><b>$75.00</b></div>
  <div class="btn">ADD TO CART</div>
</div>
<div class="card" style="left:376px;top:1362px">
  <div class="photo" role="img" aria-label="Product photo of a man in yellow boxer shorts" style="background:linear-gradient(180deg,#ececec,#c99a7a 55%,#e6d14a 78%,#ececec)"><div class="heart"><svg width="12" height="11" viewBox="0 0 12 11"><path d="M6 10L1.2 5.2A2.8 2.8 0 016 1.4a2.8 2.8 0 014.8 3.8z" fill="#fff"/></svg></div></div>
  <div class="name">Nemo enim ipsam voluptatem quia volu</div>
  <div class="price"><s>$95.00</s><b>$75.00</b></div>
  <div class="btn">ADD TO CART</div>
</div>
<div class="card" style="left:610px;top:1346px">
  <div class="photo" role="img" aria-label="Product photo of a woman in a white sports bra and briefs" style="background:linear-gradient(180deg,#e9e9e9,#d4b4a0 55%,#efefef)"><div class="heart"><svg width="12" height="11" viewBox="0 0 12 11"><path d="M6 10L1.2 5.2A2.8 2.8 0 016 1.4a2.8 2.8 0 014.8 3.8z" fill="#fff"/></svg></div></div>
  <div class="name">Nemo enim ipsam voluptatem quia volu</div>
  <div class="price"><s>$95.00</s><b>$75.00</b></div>
  <div class="btn">ADD TO CART</div>
</div>
<div class="card" style="left:844px;top:1362px">
  <div class="photo" role="img" aria-label="Product photo of a man in grey patterned trunks" style="background:linear-gradient(180deg,#ececec,#c9a088 55%,#b8bcc6 78%,#ececec)"><div class="heart"><svg width="12" height="11" viewBox="0 0 12 11"><path d="M6 10L1.2 5.2A2.8 2.8 0 016 1.4a2.8 2.8 0 014.8 3.8z" fill="#fff"/></svg></div></div>
  <div class="name">Nemo enim ipsam voluptatem quia volu</div>
  <div class="price"><s>$95.00</s><b>$75.00</b></div>
  <div class="btn">ADD TO CART</div>
</div>

<!-- sale banner -->
<section class="sale" role="img" aria-label="Photo of a woman in a floral bikini sitting on a sandy beach">
  <div class="sale-word" style="left:730px;top:57px">SALE</div>
  <div class="sale-word" style="left:682px;top:164px">OFFER</div>
</section>
<div class="badge">
  <div style="margin-top:44px;font-size:42px;font-weight:500;line-height:42px">FLAT</div>
  <div style="font-size:70px;font-weight:500;line-height:70px">35<span style="font-size:18px;vertical-align:28px;margin-left:-34px">Off</span><span style="font-size:42px">%</span></div>
</div>

<!-- about -->
<section class="about" role="img" aria-label="Photo of a woman in a black lace bustier set in a garden"></section>
<div class="about-frame"></div>
<div class="about-box">
  <h2>Velora fashion - 20 years with you</h2>
  <p>At the location of the busiest shopping center in Brenvik - Alder Court center, the Velora casa boutique has been operating for 20 years. The store offers a large selection of favorite high-quality fashion lingerie brands for women, men and children.</p>
  <div class="btn">LEARN MORE</div>
</div>

<!-- best selling -->
<h2 class="sec-title" style="top:3039px">BEST SELLING</h2>
<div class="sec-rule" style="top:3103px"></div>
<div class="arrow dark" style="left:75px;top:3313px"><svg width="32" height="32" viewBox="0 0 32 32"><path d="M18 10l-6 6 6 6" stroke="#444" stroke-width="1.6" fill="none"/></svg></div>
<div class="arrow dark" style="left:1090px;top:3313px"><svg width="32" height="32" viewBox="0 0 32 32"><path d="M14 10l6 6-6 6" stroke="#444" stroke-width="1.6" fill="none"/></svg></div>

<div class="card" style="left:142px;top:3174px">
  <div class="photo" role="img" aria-label="Product photo of a woman in a white robe on pink background" style="height:194px;background:linear-gradient(180deg,#e9a6b0,#d9887f 45%,#f2e8ea)"><div class="heart"><svg width="12" height="11" viewBox="0 0 12 11"><path d="M6 10L1.2 5.2A2.8 2.8 0 016 1.4a2.8 2.8 0 014.8 3.8z" fill="#fff"/></svg></div></div>
  <div class="name">Nemo enim ipsam voluptatem quia volu</div>
  <div class="price"><s>$95.00</s><b>$75.00</b></div>
  <div class="btn">ADD TO CART</div>
</div>
<div class="card" style="left:376px;top:3158px">
  <div class="photo" role="img" aria-label="Product photo of nude seamless briefs" style="height:194px;background:linear-gradient(180deg,#f4f4f4,#f0c4a4 50%,#f4f4f4)"><div class="heart"><svg width="12" height="11" viewBox="0 0 12 11"><path d="M6 10L1.2 5.2A2.8 2.8 0 016 1.4a2.8 2.8 0 014.8 3.8z" fill="#fff"/></svg></div></div>
  <div class="name">Nemo enim ipsam voluptatem quia volu</div>
  <div class="price"><s>$95.00</s><b>$75.00</b></div>
  <div class="btn">ADD TO CART</div>
</div>
<div class="card" style="left:610px;top:3174px">
  <div class="photo" role="img" aria-label="Product photo of a child in colourful pyjamas" style="height:194px;background:linear-gradient(180deg,#eeeeee,#e7c2a6 45%,#e65c9e)"><div class="heart"><svg width="12" height="11" viewBox="0 0 12 11"><path d="M6 10L1.2 5.2A2.8 2.8 0 016 1.4a2.8 2.8 0 014.8 3.8z" fill="#fff"/></svg></div></div>
  <div class="name">Nemo enim ipsam voluptatem quia volu</div>
  <div class="price"><s>$95.00</s><b>$75.00</b></div>
  <div class="btn">ADD TO CART</div>
</div>
<div class="card" style="left:844px;top:3158px">
  <div class="photo" role="img" aria-label="Product photo of a blush lace bra" style="height:194px;background:linear-gradient(180deg,#f5f5f5,#eac6b8 50%,#f5f5f5)"><div class="heart"><svg width="12" height="11" viewBox="0 0 12 11"><path d="M6 10L1.2 5.2A2.8 2.8 0 016 1.4a2.8 2.8 0 014.8 3.8z" fill="#fff"/></svg></div></div>
  <div class="name">Nemo enim ipsam voluptatem quia volu</div>
  <div class="price"><s>$95.00</s><b>$75.00</b></div>
  <div class="btn">ADD TO CART</div>
</div>

<!-- blog -->
<section class="blog">
  <h2 class="sec-title" style="top:56px">FROM THE BLOG</h2>
  <div class="sec-rule" style="top:120px"></div>
</section>
<article class="post" style="left:156px">
  <div class="photo" role="img" aria-label="Photo of a woman in a pale blue lingerie set outdoors" style="background:linear-gradient(90deg,#98a67a,#c9c2ae 45%,#bdd0e2 70%,#a9b58e)"></div>
  <div class="date">02<small>JUN</small></div>
  <h3>Discount on Women's Day with code: 15postodanzena</h3>
  <div class="meta"><span><i>&#9675;</i>2 comments</span><span><i>&#9998;</i>by David</span></div>
  <p>take advantage of a 15% discount on our webshop and in our store at the Alder Court Center on the occasion of International Women's Day.</p>
  <div class="btn">READ MORE &#10140;</div>
</article>
<article class="post" style="left:620px">
  <div class="photo" role="img" aria-label="Photo of a woman in a turquoise lace lingerie set" style="background:linear-gradient(90deg,#8a9c8a,#c9b3a2 40%,#5fb4c4 60%,#a8b2a8)"></div>
  <div class="date">02<small>JUN</small></div>
  <h3>Discount for Valentine's Day with code: 15% VALENTINE'S DAY</h3>
  <div class="meta"><span><i>&#9675;</i>2 comments</span><span><i>&#9998;</i>by David</span></div>
  <p>take advantage of a 15% discount on our webshop and in our store at the Alder Court Center on the occasion of International Women's Day.</p>
  <div class="btn">READ MORE &#10140;</div>
</article>

<!-- newsletter -->
<section class="news">
  <h2>JOIN OUR NEWSLETTER</h2>
  <p>Subscribe to our mailing list to receive updates and promotional offers.</p>
  <div class="field">Enter your E - mail</div>
  <div class="btn">SUBSCRIBE</div>
  <div class="photo" role="img" aria-label="Photo of three laughing women in striped pyjamas" style="left:780px;top:10px;width:320px;height:322px;background:linear-gradient(180deg,#f48a93,#e9b49a 35%,#e4dbe6 70%,#cfd4e6)"></div>
</section>

<!-- footer -->
<footer class="footer">
  <h4 style="left:142px">CONTACT US</h4>
  <h4 style="left:438px">INFORMATION</h4>
  <h4 style="left:626px">MY ACCOUNT</h4>
  <ul style="left:440px"><li>Women</li><li>Men</li><li>Children</li><li>About Us</li><li>Contact</li></ul>
  <ul style="left:626px"><li>Payment methods</li><li>Delivery</li><li>Returns and replacements</li><li>Terms of purchase</li><li>Security payment</li></ul>
  <div class="abs" style="left:850px;top:60px;font-weight:300;font-size:28px;letter-spacing:1px;color:#fff">VELORA CASA</div>
</footer>
<div class="contact" style="top:4792px"><svg width="16" height="20" viewBox="0 0 16 20"><path d="M8 0a7 7 0 017 7c0 5-7 13-7 13S1 12 1 7a7 7 0 017-7z" fill="#fff"/><circle cx="8" cy="7" r="2.6" fill="#1d1d1d"/></svg><div style="font-size:12px;line-height:17px">ADDRESS<br>PO Box 14 Lindale, CT 06210</div></div>
<div class="contact" style="top:4836px"><svg width="18" height="18" viewBox="0 0 12 12"><path d="M2.5 1l2 2.5-1 1.5c.7 1.5 1.8 2.6 3.3 3.3l1.5-1 2.5 2-1 2C5 11 1 7 .8 2z" fill="#fff"/></svg><div>Phone: 01 / 5830-217</div></div>
<div class="contact" style="top:4870px"><svg width="18" height="14" viewBox="0 0 18 14"><rect width="18" height="14" rx="1" fill="#fff"/><path d="M1 1l8 6 8-6" stroke="#1d1d1d" stroke-width="1.5" fill="none"/></svg><div>E-mail: info@veloracasa.hr</div></div>
<div class="contact" style="top:4906px"><svg width="18" height="18" viewBox="0 0 18 18"><circle cx="9" cy="9" r="9" fill="#fff"/><path d="M9 4v5l3 3" stroke="#1d1d1d" stroke-width="1.8" fill="none"/></svg><div style="line-height:25px">Opening hours:<br>Mon - Sat: 09 - 21 h<br>Sun: Closed</div></div>

<div class="pay" style="left:860px;background:#e9edf5"></div>
<div class="pay" style="left:912px;background:#2c2c2c;border:1px solid #666"></div>
<div class="pay" style="left:964px;background:#3a7cc4"></div>
<div class="pay" style="left:1006px;background:#f0f0f0"></div>
<div class="soc" style="left:948px"></div>
<div class="soc" style="left:986px"></div>
<div class="soc" style="left:1023px"></div>

<div class="copy">© 2020 Velora Casa. All Rights Reserved.</div>

</body>
</html>
```